Design some cool and useful Business Cards

The following should be on the business card of a business providing outdoor teambuilding activities:

Front:
* Website name: "waldkreisEvents.de"
* Business owner: "Klaus-Dieter Bramsch"
* Phone: "+49 162 738 204 61"
* Mail: "dieter@waldkreisevents.de"
* Slogan: "Waldkreis Events" (naturally different)
* Visualization of the slogan

Back:
Slogan: "Waldkreis Sicher" (naturally secure)
"Passwort Generator"
[password encoding fields (without the black signs), refer to sample on attached photo]

Size: 86x54 mm
Colors in CMYK
300 DPI

```html
<!DOCTYPE html>
<html lang="de">
<head>
<meta charset="utf-8">
<title>Waldkreis Events – Visitenkarte</title>
<link rel="stylesheet" href="https://fonts.googleapis.com/css2?family=Tinos:wght@400;700&family=Arimo:wght@400&display=swap">
<style>
  :root {
    --stage: #ecebe8;
    --card: #ffffff;
    --green: #1f6b2a;
    --green-dark: #14501d;
    --ink: #1b1b1b;
    --map-light: #eef2fa;
    --map-mid: #c9d3ec;
    --map-warm: #f1cfc9;
    --field-border: #2a2a2a;
    --shadow: rgba(0,0,0,0.22);
  }
  * { margin: 0; padding: 0; box-sizing: border-box; }
  html, body { width: 1200px; height: 675px; overflow: hidden; }
  body {
    background: var(--stage);
    position: relative;
    font-family: "Arimo", Arial, sans-serif;
  }
  .card {
    position: absolute;
    top: 174px;
    width: 520px;
    height: 327px;
    background: var(--card);
    box-shadow: 0 6px 18px var(--shadow);
    overflow: hidden;
  }
  .card-back { left: 50px; }
  .card-front { left: 630px; }

  /* Back */
  .world-map {
    position: absolute; inset: 0;
    background:
      radial-gradient(ellipse 22% 18% at 62% 42%, var(--map-warm), transparent 70%),
      radial-gradient(ellipse 18% 14% at 30% 60%, var(--map-warm), transparent 70%),
      linear-gradient(160deg, var(--map-mid), var(--map-light) 45%, var(--map-mid));
  }
  .back-title {
    position: absolute; top: 78px; left: 0; right: 0;
    text-align: center;
    font-family: "Tinos", "Times New Roman", serif;
    font-weight: 700;
    font-size: 30px;
    letter-spacing: 2px;
    color: var(--green);
  }
  .password-fields {
    position: absolute; top: 218px; left: 20px; right: 20px;
    display: flex; justify-content: space-between;
  }
  .field { width: 46px; text-align: center; }
  .field-box {
    height: 22px;
    background: var(--card);
    border: 2px solid var(--field-border);
    border-radius: 2px;
  }
  .field-label {
    margin-top: 5px;
    font-family: "Tinos", "Times New Roman", serif;
    font-weight: 700;
    font-size: 9px;
    color: var(--ink);
  }

  /* Front */
  .owner-name {
    position: absolute; top: 30px; left: 34px;
    font-family: "Tinos", "Times New Roman", serif;
    font-weight: 400;
    font-size: 21px;
    color: var(--green);
    text-transform: uppercase;
  }
  .owner-role {
    position: absolute; top: 56px; left: 34px;
    font-family: "Tinos", "Times New Roman", serif;
    font-size: 11px;
    color: var(--green);
    text-transform: uppercase;
  }
  .contact-list {
    position: absolute; top: 140px; left: 34px;
    list-style: none;
  }
  .contact-item {
    display: flex; align-items: center; gap: 12px;
    height: 34px;
    font-size: 15px;
    color: var(--green-dark);
  }
  .contact-icon { width: 20px; height: 20px; flex: none; }
  .brand {
    position: absolute; top: 135px; left: 330px; width: 170px;
    display: flex; flex-direction: column; align-items: center; gap: 14px;
  }
  .brand-dot {
    width: 70px; height: 70px; border-radius: 50%;
    background: var(--green);
  }
  .brand-name {
    font-family: "Tinos", "Times New Roman", serif;
    font-weight: 700;
    font-size: 20px;
    color: var(--green);
    white-space: nowrap;
  }
</style>
</head>
<body>

<section class="card card-back" aria-label="Rückseite">
  <div class="world-map" role="img" aria-label="Blasse Weltkarte als Hintergrund"></div>
  <h2 class="back-title">WALDKREIS SICHER</h2>
  <div class="password-fields">
    <div class="field"><div class="field-box"></div><div class="field-label">START</div></div>
    <div class="field"><div class="field-box"></div><div class="field-label">ABC</div></div>
    <div class="field"><div class="field-box"></div><div class="field-label">DEF</div></div>
    <div class="field"><div class="field-box"></div><div class="field-label">GHI</div></div>
    <div class="field"><div class="field-box"></div><div class="field-label">JKL</div></div>
    <div class="field"><div class="field-box"></div><div class="field-label">MNO</div></div>
    <div class="field"><div class="field-box"></div><div class="field-label">PQRS</div></div>
    <div class="field"><div class="field-box"></div><div class="field-label">TUV</div></div>
    <div class="field"><div class="field-box"></div><div class="field-label">WXYZ</div></div>
  </div>
</section>

<section class="card card-front" aria-label="Vorderseite">
  <h1 class="owner-name">Klaus-Dieter Bramsch</h1>
  <p class="owner-role">Owner</p>
  <ul class="contact-list">
    <li class="contact-item">
      <svg class="contact-icon" viewBox="0 0 20 20"><rect width="20" height="20" rx="4" fill="#1f6b2a"/><path d="M6 4.5l2.2 0 1 3-1.4 1.2a7 7 0 0 0 3.5 3.5l1.2-1.4 3 1v2.2c0 .6-.5 1-1 1A11 11 0 0 1 5 5.5c0-.6.4-1 1-1z" fill="#fff"/></svg>
      <span>+49 162 738 204 61</span>
    </li>
    <li class="contact-item">
      <svg class="contact-icon" viewBox="0 0 20 20"><circle cx="10" cy="10" r="10" fill="#1f6b2a"/><circle cx="10" cy="10" r="5.5" fill="none" stroke="#fff" stroke-width="1.4"/><path d="M4.5 10h11M10 4.5c-2.5 3-2.5 8 0 11M10 4.5c2.5 3 2.5 8 0 11" fill="none" stroke="#fff" stroke-width="1.2"/></svg>
      <span>waldkreisEvents.de</span>
    </li>
    <li class="contact-item">
      <svg class="contact-icon" viewBox="0 0 20 20"><rect y="3" width="20" height="14" rx="1.5" fill="#1f6b2a"/><path d="M1.5 4.5l8.5 7 8.5-7" fill="none" stroke="#fff" stroke-width="1.4"/></svg>
      <span>dieter@waldkreisevents.de</span>
    </li>
  </ul>
  <div class="brand">
    <div class="brand-dot"></div>
    <div class="brand-name">Waldkreis Events</div>
  </div>
</section>

</body>
</html>
```